Marcus Lindqvist Photography needs a business card designs

I am looking for a business card with a logo clean and simple which I can use that logo on my website or on my pictures. It has to be very classy and very professional. Please look at my website at www.marcuslvqphoto.com for my signature. I'm thinking of something like that for my signature/logo. I'm still working on my website but you get an idea. I'm open to any design but not too busy graphics.

I will be printing the business card from qrivel.com.

Surprise me :)

contact me if you have any questions.

-ML

I'm receiving a lot of black background at the moment. I know my website is all black doesn't mean I want my card to be all black. Please send in with some white background as well. Thanks :)

check out some business cards that I found online. I think they are simple and look really awesome. I don't want a card that is too busy.

http://www.marcuslvqphoto.com/p270092084

Reason: Please extend the date for me. I haven't really receive any good design yet.

Printing

• -a logo that related to my first and last initial of my name "ML"
-double sided
• -I don't want my background to be all black.
-no pictures on the card

```html
<!DOCTYPE html>
<html lang="en">
<head>
<meta charset="utf-8">
<title>Marcus Lindqvist Photography — Business Card</title>
<link rel="stylesheet" href="https://fonts.googleapis.com/css2?family=Italianno&family=Josefin+Sans:wght@300&family=Arimo:ital,wght@0,400;0,700;1,400&display=swap">
<style>
  :root {
    --canvas: #ffffff;
    --card-front: #ffffff;
    --card-edge: #b9b9b9;
    --back-light: #ffffff;
    --back-mid: #ececec;
    --back-dark: #bdbdbd;
    --ink: #3a3a3a;
    --ink-soft: #6a6a6a;
    --mark: #d6d6d6;
    --mark-ring: #9a9a9a;
  }
  * { margin: 0; padding: 0; box-sizing: border-box; }
  html, body {
    width: 1200px; height: 1200px; overflow: hidden;
    background: var(--canvas);
  }
  .stage { position: relative; width: 1200px; height: 1200px; }

  .card {
    position: absolute;
    top: 120px;
    width: 566px;
    height: 907px;
    border-radius: 32px;
    border: 2px solid var(--card-edge);
    box-shadow: 3px 6px 10px rgba(0,0,0,0.18);
    overflow: hidden;
  }

  /* Front */
  .card-front { left: 21px; background: var(--card-front); }
  .brand-mark {
    position: absolute; left: 150px; top: 93px;
    width: 266px; height: 266px;
  }
  .brand-name {
    position: absolute; left: 0; right: 0; top: 470px;
    text-align: center;
    font-family: "Josefin Sans", sans-serif;
    font-weight: 300;
    color: var(--ink-soft);
    text-transform: uppercase;
  }
  .brand-name .line-name { display: block; font-size: 44px; letter-spacing: 4px; }
  .brand-name .line-trade { display: block; font-size: 30px; letter-spacing: 9px; margin-top: 14px; }

  /* Back */
  .card-back {
    left: 613px;
    background: radial-gradient(ellipse 85% 70% at 72% 42%, var(--back-light) 0%, var(--back-mid) 55%, var(--back-dark) 100%);
  }
  .contact-block {
    position: absolute; left: 52px; top: 570px;
    padding-left: 10px;
    border-left: 2px solid var(--ink-soft);
  }
  .person-name {
    font-family: "Italianno", cursive;
    font-size: 78px; line-height: 0.9;
    color: var(--ink);
  }
  .person-role {
    font-family: "Arimo", sans-serif;
    font-style: italic;
    font-size: 23px;
    color: var(--ink-soft);
    margin-bottom: 34px;
  }
  .contact-list { list-style: none; font-family: "Arimo", sans-serif; font-size: 26px; color: var(--ink); line-height: 35px; }
  .contact-list b { font-weight: 700; }
</style>
</head>
<body>
<main class="stage">
  <section class="card card-front" aria-label="Card front">
    <svg class="brand-mark" viewBox="0 0 266 266" aria-hidden="true">
      <circle cx="133" cy="133" r="130" fill="var(--mark)" stroke="var(--mark-ring)" stroke-width="3"/>
    </svg>
    <h1 class="brand-name">
      <span class="line-name">Marcus Lindqvist</span>
      <span class="line-trade">Photography</span>
    </h1>
  </section>

  <section class="card card-back" aria-label="Card back">
    <div class="contact-block">
      <p class="person-name">Marcus Lindqvist</p>
      <p class="person-role">professional photographer</p>
      <ul class="contact-list">
        <li><b>p:</b> 0400 318 527</li>
        <li><b>e:</b> mail@marcuslvqphoto.com</li>
        <li><b>w:</b> www.marcuslvqphoto.com</li>
      </ul>
    </div>
  </section>
</main>
</body>
</html>
```